Need Letterhead Design & Matching Business Card

I have a logo that I love already. But the letterhead is less than appealing and boring. I'd like a design for my letterhead which I will match with business cards. Also, I'd like to have used fonts that are generally available, as my current letterhead uses a font named "SPACE" which nobody has unless they download it...so when a Word version is forwarded, it looks awful on the receiver's screed due to not having the font. That being said, modern is the look we like and are going for.

My business is "Hollister Brantley PC" - a law firm specializing in representing people who have suffered catastrophic injuries or death (plane, auto, train crashes etc.).

See attached letterhead, which has all of the pertinent information. My logo is also attached in various formats.

```html
<!DOCTYPE html>
<html lang="en">
<head>
<meta charset="utf-8">
<title>Hollister Brantley PC – Stationery</title>
<link href="https://fonts.googleapis.com/css2?family=Archivo:wght@600&family=Arimo:wght@400;700&display=swap" rel="stylesheet">
<style>
  :root {
    --ink: #0a0a0a;
    --paper: #ffffff;
    --backdrop: #ffffff;
    --rule: #8a8a8a;
    --shadow: 0 4px 10px rgba(0,0,0,0.28);
  }
  * { margin: 0; padding: 0; box-sizing: border-box; }
  html, body { width: 1200px; height: 1200px; overflow: hidden; background: var(--backdrop); }
  .canvas { position: relative; width: 1200px; height: 1200px; font-family: "Arimo", Arial, sans-serif; color: var(--ink); }

  .sheet { position: absolute; background: var(--paper); box-shadow: var(--shadow); overflow: hidden; }
  .sheet.dark { background: var(--ink); color: var(--paper); }

  /* wordmark */
  .brand { position: absolute; display: flex; align-items: center; }
  .brand-square { background: var(--ink); flex: none; }
  .dark .brand-square { background: var(--paper); }
  .brand-name { font-family: "Archivo", Arial, sans-serif; font-weight: 600; text-transform: uppercase; letter-spacing: 0.06em; line-height: 1.08; }
  .brand-name .suffix { font-size: 0.42em; letter-spacing: 0.08em; margin-left: 0.15em; }

  /* contact list */
  .contacts { position: absolute; list-style: none; }
  .contacts li { display: flex; align-items: center; }
  .contacts svg { flex: none; }

  .address-line { position: absolute; font-weight: 700; text-transform: uppercase; white-space: nowrap; letter-spacing: 0.01em; }

  /* letterhead */
  .letterhead { left: 50px; top: 74px; width: 526px; height: 680px; }
  .letterhead .brand { left: 22px; top: 19px; }
  .letterhead .brand-square { width: 42px; height: 42px; margin-right: 6px; }
  .letterhead .brand-name { font-size: 14px; }
  .letterhead .contacts { left: 370px; top: 22px; font-size: 10px; }
  .letterhead .contacts li { height: 18px; }
  .letterhead .contacts svg { width: 11px; height: 11px; margin-right: 7px; }
  .letterhead-footer { position: absolute; left: 0; bottom: 0; width: 100%; height: 35px; background: var(--ink); color: var(--paper); }
  .letterhead-footer .address-line { left: 27px; top: 12px; font-size: 9.4px; }

  /* master logo */
  .master-logo { left: 700px; top: 74px; }
  .master-logo .brand-square { width: 121px; height: 121px; margin-right: 17px; }
  .master-logo .brand-name { font-size: 40px; line-height: 1.15; }

  /* business card front */
  .card-front { left: 719px; top: 283px; width: 371px; height: 211px; }
  .card-front .card-square { position: absolute; left: 258px; top: 23px; width: 89px; height: 89px; background: var(--ink); }
  .card-front .contacts { left: 18px; top: 122px; font-size: 11.5px; font-weight: 700; }
  .card-front .contacts li { height: 21px; }
  .card-front .contacts svg { width: 14px; height: 14px; margin-right: 8px; }
  .card-front .address-line { left: 18px; top: 196px; font-size: 6.4px; }

  /* business card back */
  .card-back { left: 718px; top: 543px; width: 371px; height: 211px; }
  .card-back .brand { left: 70px; top: 70px; }
  .card-back .brand-square { width: 72px; height: 72px; margin-right: 10px; }
  .card-back .brand-name { font-size: 23px; line-height: 1.2; }

  /* envelope front */
  .envelope { left: 45px; top: 881px; width: 538px; height: 239px; }
  .envelope .brand { left: 18px; top: 19px; }
  .envelope .brand-square { width: 50px; height: 50px; margin-right: 7px; }
  .envelope .brand-name { font-size: 17px; line-height: 1.15; }
  .envelope-window { position: absolute; left: 19px; top: 89px; width: 248px; height: 105px; border: 1px dashed var(--rule); border-radius: 6px; }

  /* envelope back */
  .envelope-back { left: 614px; top: 880px; width: 541px; height: 240px; }
  .envelope-back .seal-square { position: absolute; left: 232px; top: 82px; width: 77px; height: 77px; background: var(--paper); }
  .envelope-back .address-line { left: 0; width: 100%; text-align: center; top: 216px; font-size: 9.4px; }
</style>
</head>
<body>
<svg width="0" height="0" style="position:absolute" aria-hidden="true">
  <symbol id="icon-phone" viewBox="0 0 20 20">
    <circle cx="10" cy="10" r="10" fill="#0a0a0a"/>
    <rect x="7" y="4.5" width="6" height="11" rx="1.2" fill="none" stroke="#fff" stroke-width="1.4"/>
    <circle cx="10" cy="13.4" r="0.8" fill="#fff"/>
  </symbol>
  <symbol id="icon-mail" viewBox="0 0 20 20">
    <circle cx="10" cy="10" r="10" fill="#0a0a0a"/>
    <rect x="5" y="6.5" width="10" height="7" fill="#fff"/>
    <path d="M5 6.5 L10 10.5 L15 6.5" fill="none" stroke="#0a0a0a" stroke-width="1.1"/>
  </symbol>
  <symbol id="icon-web" viewBox="0 0 20 20">
    <circle cx="10" cy="10" r="10" fill="#0a0a0a"/>
    <circle cx="10" cy="10" r="5.5" fill="none" stroke="#fff" stroke-width="1.1"/>
    <ellipse cx="10" cy="10" rx="2.4" ry="5.5" fill="none" stroke="#fff" stroke-width="1"/>
    <path d="M4.5 10 H15.5 M5.3 7.4 H14.7 M5.3 12.6 H14.7" stroke="#fff" stroke-width="0.9"/>
  </symbol>
</svg>

<main class="canvas">

  <section class="sheet letterhead" aria-label="Letterhead">
    <div class="brand">
      <span class="brand-square"></span>
      <span class="brand-name">Hollister<br>Brantley<span class="suffix">PC</span></span>
    </div>
    <ul class="contacts">
      <li><svg><use href="#icon-phone"/></svg>(805) 555-0142</li>
      <li><svg><use href="#icon-mail"/></svg>dana@hollisterbrantley.com</li>
      <li><svg><use href="#icon-web"/></svg>www.hollisterbrantley.com</li>
    </ul>
    <footer class="letterhead-footer">
      <p class="address-line">Dana Ortiz, Esq. &nbsp;|&nbsp; President 4410 Hollister Ave. &nbsp;|&nbsp; Suite 300 Santa Barbara, CA 93110</p>
    </footer>
  </section>

  <div class="brand master-logo">
    <span class="brand-square"></span>
    <span class="brand-name">Hollister<br>Brantley<span class="suffix">PC</span></span>
  </div>

  <section class="sheet card-front" aria-label="Business card front">
    <span class="card-square"></span>
    <ul class="contacts">
      <li><svg><use href="#icon-phone"/></svg>(805) 555-0142</li>
      <li><svg><use href="#icon-mail"/></svg>dana@hollisterbrantley.com</li>
      <li><svg><use href="#icon-web"/></svg>www.hollisterbrantley.com</li>
    </ul>
    <p class="address-line">Dana Ortiz, Esq. &nbsp;|&nbsp; President 4410 Hollister Ave. &nbsp;|&nbsp; Suite 300 Santa Barbara, CA 93110</p>
  </section>

  <section class="sheet dark card-back" aria-label="Business card back">
    <div class="brand">
      <span class="brand-square"></span>
      <span class="brand-name">Hollister<br>Brantley<span class="suffix">PC</span></span>
    </div>
  </section>

  <section class="sheet envelope" aria-label="Envelope front">
    <div class="brand">
      <span class="brand-square"></span>
      <span class="brand-name">Hollister<br>Brantley<span class="suffix">PC</span></span>
    </div>
    <div class="envelope-window"></div>
  </section>

  <section class="sheet dark envelope-back" aria-label="Envelope back">
    <span class="seal-square"></span>
    <p class="address-line">Dana Ortiz, Esq. &nbsp;|&nbsp; President 4410 Hollister Ave. &nbsp;|&nbsp; Suite 300 Santa Barbara, CA 93110</p>
  </section>

</main>
</body>
</html>
```